New Zealand Export company needs business cards

We need new business cards to match our new logo for a company based in New Zealand who deal specifically with the Pacific Islands. We source, consolidate and ship products out of New Zealand to the Pacific Islands. Will attach our old ones and also new logo.
Would like the Islands we deal with and the areas of work we have access to, to be included on the business cards.

Contact Information for Business Card

T +64 9 571 3048
F +64 9 571 6285
12-18 Kowhai Lane, Drury, 2113
PO Box 814, Drury, Auckland 2247, New Zealand
www.falconfreight.example.nz
E sales@falconfreight.example.nz

Font styles to use
Sans Serif

Colors
85abd2
33a6d7
ffffff

Requirements
Must have
• A company of PWM

```html
<!DOCTYPE html>
<html lang="en">
<head>
<meta charset="utf-8">
<title>Falcon Freight Business Cards</title>
<link rel="stylesheet" href="https://fonts.googleapis.com/css2?family=Work+Sans:wght@400;500;600&display=swap">
<style>
  :root {
    --page-bg: #141414;
    --card-bg: #262627;
    --card-edge: #1b64b8;
    --brand-blue: #1f6fc4;
    --brand-sky: #33a6d7;
    --soft-blue: #85abd2;
    --silver: #a3a3a5;
    --text-light: #ffffff;
  }
  * { margin: 0; padding: 0; box-sizing: border-box; }
  html, body { width: 1200px; height: 900px; overflow: hidden; }
  body {
    background: radial-gradient(ellipse at 60% 40%, #2a2a2a 0%, var(--page-bg) 70%);
    font-family: "Work Sans", sans-serif;
    color: var(--text-light);
    position: relative;
  }
  .card {
    position: absolute;
    left: 250px;
    width: 700px;
    height: 400px;
    background: radial-gradient(ellipse at 70% 40%, #323233 0%, var(--card-bg) 75%);
    border-bottom: 6px solid var(--card-edge);
    box-shadow: 0 18px 40px rgba(0,0,0,0.6);
  }
  .card--front { top: 40px; }
  .card--back { top: 470px; }

  .wordmark {
    display: flex;
    align-items: center;
    gap: 16px;
    font-weight: 600;
    letter-spacing: 3px;
    text-transform: uppercase;
  }
  .wordmark__square { width: 34px; height: 34px; flex: none; }
  .card--front .wordmark {
    position: absolute;
    left: 50%; top: 50%;
    transform: translate(-50%, -50%);
    font-size: 46px;
    color: var(--silver);
    white-space: nowrap;
  }
  .card--front .wordmark__square { background: var(--silver); }

  .card--back .wordmark {
    position: absolute;
    left: 46px; top: 170px;
    font-size: 30px;
    color: var(--brand-sky);
    white-space: nowrap;
  }
  .card--back .wordmark__square { width: 26px; height: 26px; background: var(--brand-sky); }

  .divider {
    position: absolute;
    left: 390px; top: 48px;
    width: 2px; height: 290px;
    background: var(--brand-blue);
  }
  .contact {
    position: absolute;
    left: 418px; top: 46px;
    width: 270px;
  }
  .contact__name {
    font-size: 30px;
    font-weight: 500;
    color: var(--brand-blue);
    letter-spacing: 1.5px;
    text-transform: uppercase;
    line-height: 1;
  }
  .contact__role {
    font-size: 17px;
    margin-top: 6px;
    letter-spacing: 0.5px;
  }
  .contact__list {
    list-style: none;
    margin-top: 16px;
    font-size: 14.5px;
    line-height: 1.6;
  }
  .contact__list li { display: flex; align-items: center; gap: 8px; white-space: nowrap; }
  .contact__list svg { width: 12px; height: 12px; flex: none; }
  .contact__address {
    margin-top: 14px;
    font-size: 15.5px;
    line-height: 1.5;
    font-style: normal;
  }
</style>
</head>
<body>
  <section class="card card--front" aria-label="Card front">
    <div class="wordmark"><span class="wordmark__square"></span>Falcon Freight</div>
  </section>

  <section class="card card--back" aria-label="Card back">
    <div class="wordmark"><span class="wordmark__square"></span>Falcon Freight</div>
    <div class="divider"></div>
    <div class="contact">
      <h1 class="contact__name">Daniel Reeve</h1>
      <p class="contact__role">Managing Partner</p>
      <ul class="contact__list">
        <li>
          <svg viewBox="0 0 12 12" aria-hidden="true"><path d="M3 1 L5 3.5 L4 5 Q5.5 7.5 7 8 L8.5 7 L11 9 L9.5 11 Q4 10.5 1 3 Z" fill="var(--brand-blue)"/></svg>
          +64 9 571 3048
        </li>
        <li>
          <svg viewBox="0 0 12 12" aria-hidden="true"><rect x="2" y="1" width="8" height="4" fill="none" stroke="var(--brand-blue)" stroke-width="1.2"/><rect x="1" y="5" width="10" height="5" rx="1" fill="var(--brand-blue)"/></svg>
          +64 9 571 6285
        </li>
        <li>
          <svg viewBox="0 0 12 12" aria-hidden="true"><rect x="1" y="2.5" width="10" height="7" fill="none" stroke="var(--brand-blue)" stroke-width="1.2"/><path d="M1 2.5 L6 6.5 L11 2.5" fill="none" stroke="var(--brand-blue)" stroke-width="1.2"/></svg>
          sales@falconfreight.example.nz
        </li>
        <li>
          <svg viewBox="0 0 12 12" aria-hidden="true"><circle cx="6" cy="6" r="5" fill="none" stroke="var(--brand-blue)" stroke-width="1.2"/><ellipse cx="6" cy="6" rx="2.2" ry="5" fill="none" stroke="var(--brand-blue)" stroke-width="1"/><path d="M1 6 H11" stroke="var(--brand-blue)" stroke-width="1"/></svg>
          www.falconfreight.example.nz
        </li>
      </ul>
      <address class="contact__address">
        12-18 Kowhai Lane, Drury, 2113<br>
        PO Box 814, Drury,<br>
        Auckland 2247, New Zealand
      </address>
    </div>
  </section>
</body>
</html>
```